Life and business Coaching Business Card and Logo

A new design for new company. We coach people to get the best out of themselves in business, life, health , family, career, relationships.
we work in Professional, executive, business and corporate environment. We use art and the processes of making art to work with getting people to delve into and change their mind maps or the way they are currently thinking so that they can move forward towards their goals strategically.
Updates

Project Deadline Extended
Reason: I have been laid up in bed with back problems and have just been able to get back to view designs. several are quiet good and I have given feedback today. I also want to take my project off refundable status as I will choose a design from this brief. regards Rosalind

Target Market(s)

Professional artistic and bold energetic individuals

Industry/Entity Type

Health

Contact Information for Business Card

Northwind Growth, Rosalind Pettigrew, Shaping Days Boldly,
Mob:0412958176, Ph: +61 8 93627580,
Professional, Executive, Business and Corporate Coach

Requirements
Must have
• a logo that can be used on all promotional and stationary material.
Should contain a person and be bold/colourful, simple and artistic.
Nice to have
• Room to place qualifications of Business

```html
<!DOCTYPE html>
<html lang="en">
<head>
<meta charset="utf-8">
<title>Northwind Growth – Business Card</title>
<link rel="stylesheet" href="https://fonts.googleapis.com/css2?family=Delius&display=swap">
<style>
  :root {
    --card-bg: #3a1515;
    --hot-pink: #ff0a6c;
    --mint: #14f79a;
  }
  html, body {
    margin: 0;
    padding: 0;
    width: 1200px;
    height: 741px;
    overflow: hidden;
    background: var(--card-bg);
  }
  .business-card {
    display: block;
    width: 1200px;
    height: 741px;
    font-family: "Delius", "Comic Sans MS", cursive;
  }
  .card-bg { fill: var(--card-bg); }
  .band-edge { fill: var(--hot-pink); }
  .band-fill { fill: var(--mint); }
  .qualification { fill: var(--mint); font-size: 46px; }
  .brand-mark { fill: var(--mint); }
  .brand-name { fill: var(--hot-pink); font-size: 74px; }
  .person-name { fill: var(--hot-pink); font-size: 44px; }
  .tagline { fill: var(--mint); font-size: 32px; }
  .role-line { fill: var(--hot-pink); font-size: 44px; }
  .contact { fill: var(--mint); font-size: 31px; }
</style>
</head>
<body>
<svg class="business-card" viewBox="0 0 1200 741" xmlns="http://www.w3.org/2000/svg">
  <rect class="card-bg" x="0" y="0" width="1200" height="741"/>

  <!-- cross bands -->
  <rect class="band-edge" x="56" y="0" width="106" height="741"/>
  <rect class="band-edge" x="0" y="551" width="1200" height="108"/>
  <rect class="band-fill" x="67" y="0" width="84" height="741"/>
  <rect class="band-fill" x="0" y="562" width="1200" height="84"/>

  <!-- qualifications list -->
  <g class="qualifications">
    <text class="qualification" x="264" y="72" textLength="333" lengthAdjust="spacingAndGlyphs">Qualifications</text>
    <text class="qualification" x="264" y="180" textLength="333" lengthAdjust="spacingAndGlyphs">Qualifications</text>
    <text class="qualification" x="264" y="288" textLength="333" lengthAdjust="spacingAndGlyphs">Qualifications</text>
    <text class="qualification" x="264" y="396" textLength="333" lengthAdjust="spacingAndGlyphs">Qualifications</text>
    <text class="qualification" x="264" y="504" textLength="333" lengthAdjust="spacingAndGlyphs">Qualifications</text>
  </g>

  <!-- brand -->
  <g class="brand">
    <circle class="brand-mark" cx="965" cy="130" r="68"/>
    <text class="brand-name" x="1172" y="300" text-anchor="end" textLength="400" lengthAdjust="spacingAndGlyphs">Northwind</text>
    <text class="brand-name" x="1172" y="380" text-anchor="end" textLength="260" lengthAdjust="spacingAndGlyphs">Growth</text>
  </g>

  <text class="person-name" x="786" y="484" textLength="389" lengthAdjust="spacingAndGlyphs">Rosalind Pettigrew</text>
  <text class="tagline" x="800" y="530" textLength="375" lengthAdjust="spacingAndGlyphs">Shaping Days Boldly</text>

  <text class="role-line" x="11" y="621" textLength="1178" lengthAdjust="spacingAndGlyphs">Professional, Executive, Business and Corporate Coach</text>

  <g class="contacts">
    <text class="contact" x="205" y="713" textLength="270" lengthAdjust="spacingAndGlyphs">Ph: +61 8 93627580</text>
    <text class="contact" x="512" y="713" textLength="385" lengthAdjust="spacingAndGlyphs">www.northwindgrowth.com.au</text>
    <text class="contact" x="930" y="713" textLength="240" lengthAdjust="spacingAndGlyphs">Mob:0412958176</text>
  </g>
</svg>
</body>
</html>
```